Penrow Insights - what matters when choosing suppliers

We are a consultancy firm called Penrow Insights specializing in customer strategies. We would like to a more illustrative design of the attached graphic.

The graph shows what is important for B2B companies when choosing suppliers. On the left we have the statistical importance and on the right we have the "asked" importance ("on a scale from 1-10, how important is...." ).

Hope it makes sense! :-)

Target Market(s)

B2B Companies

Industry/Entity Type

Business Consultant

```html
<!DOCTYPE html>
<html lang="en">
<head>
<meta charset="utf-8">
<title>Penrow Insights – Importance of business drivers</title>
<link href="https://fonts.googleapis.com/css2?family=Source+Sans+3:wght@400;500&display=swap" rel="stylesheet">
<style>
  :root {
    --page: #ffffff;
    --panel: #e8dcb8;
    --ink: #111111;
    --calc-front: #ff0a0a;
    --calc-top: #e81212;
    --calc-side: #c81414;
    --asked-front: #8eaae2;
    --asked-top: #7b95c4;
    --asked-side: #6f8ab6;
  }
  html, body {
    margin: 0;
    padding: 0;
    width: 1200px;
    height: 1000px;
    overflow: hidden;
    background: var(--page);
    font-family: "Source Sans 3", "Myriad Pro", Arial, sans-serif;
    color: var(--ink);
  }
  .canvas { position: relative; width: 1200px; height: 1000px; }
  .panel {
    position: absolute; left: 86px; top: 97px;
    width: 1027px; height: 805px;
    background: var(--panel);
  }
  .chart { position: absolute; left: 0; top: 0; }
  .title {
    position: absolute; left: 168px; top: 132px; margin: 0;
    font-size: 25px; font-weight: 500; letter-spacing: -0.2px;
  }
  .col-head {
    position: absolute; top: 178px; margin: 0;
    font-size: 18.5px; font-weight: 400;
    transform: translateX(-50%); white-space: nowrap;
  }
  .col-head.calculated { left: 352px; }
  .col-head.asked { left: 840px; }
  .driver {
    position: absolute; left: 598px; margin: 0;
    transform: translate(-50%, -50%);
    font-size: 18.5px; text-align: center; line-height: 23px;
  }
  .calc .front { fill: var(--calc-front); }
  .calc .top { fill: var(--calc-top); }
  .calc .side { fill: var(--calc-side); }
  .asked-bar .front { fill: var(--asked-front); }
  .asked-bar .top { fill: var(--asked-top); }
  .asked-bar .side { fill: var(--asked-side); }
  .notes {
    position: absolute; left: 158px; top: 776px; width: 930px;
    margin: 0; padding: 0; list-style: none;
    font-size: 17px; line-height: 24px;
  }
  .notes li { padding-left: 14px; text-indent: -14px; margin-bottom: 6px; }
</style>
</head>
<body>
<div class="canvas">
  <div class="panel"></div>

  <svg class="chart" width="1200" height="1000" viewBox="0 0 1200 1000" role="img" aria-label="Bar chart comparing calculated and asked importance of five business drivers">
    <!-- Calculated importance -->
    <g class="calc">
      <polygon class="top" points="218,242 468,231 485,241 235,252"/>
      <polygon class="side" points="218,242 235,252 235,284 218,275"/>
      <polygon class="front" points="235,252 485,241 485,272 235,284"/>

      <polygon class="top" points="236,352 472,332 485,340 248,362"/>
      <polygon class="side" points="236,352 248,362 248,393 236,383"/>
      <polygon class="front" points="248,362 485,340 485,378 248,393"/>

      <polygon class="top" points="385,447 472,440 485,447 396,452"/>
      <polygon class="side" points="385,447 396,452 396,486 385,477"/>
      <polygon class="front" points="396,452 485,447 485,479 396,486"/>

      <polygon class="top" points="408,545 477,537 485,545 416,548"/>
      <polygon class="side" points="408,545 416,548 416,584 408,576"/>
      <polygon class="front" points="416,548 485,545 485,577 416,584"/>

      <polygon class="top" points="460,642 478,639 485,647 470,648"/>
      <polygon class="side" points="460,642 470,648 470,685 460,677"/>
      <polygon class="front" points="470,648 485,647 485,684 470,685"/>
    </g>

    <!-- Asked importance -->
    <g class="asked-bar">
      <polygon class="top" points="702,242 715,232 918,243 905,253"/>
      <polygon class="front" points="702,242 905,253 905,284 702,271"/>
      <polygon class="side" points="905,253 918,243 918,272 905,284"/>

      <polygon class="top" points="702,349 714,341 733,342 720,350"/>
      <polygon class="front" points="702,349 720,350 720,385 702,384"/>
      <polygon class="side" points="720,350 733,342 733,374 720,385"/>

      <polygon class="top" points="702,450 716,441 837,448 824,456"/>
      <polygon class="front" points="702,450 824,456 824,486 702,479"/>
      <polygon class="side" points="824,456 837,448 837,476 824,486"/>

      <polygon class="top" points="702,540 716,530 975,546 962,556"/>
      <polygon class="front" points="702,540 962,556 962,591 702,576"/>
      <polygon class="side" points="962,556 975,546 975,578 962,591"/>

      <polygon class="top" points="702,648 716,638 842,645 829,654"/>
      <polygon class="front" points="702,648 829,654 829,686 702,678"/>
      <polygon class="side" points="829,654 842,645 842,674 829,686"/>
    </g>
  </svg>

  <h1 class="title">Figure 1. Importance of business drivers</h1>
  <h2 class="col-head calculated">Calculated importance *</h2>
  <h2 class="col-head asked">Asked importance **</h2>

  <p class="driver" style="top:257px">Products</p>
  <p class="driver" style="top:362px">Brand</p>
  <p class="driver" style="top:462px">Advice</p>
  <p class="driver" style="top:560px">Delivery</p>
  <p class="driver" style="top:664px">Customer<br>Service</p>

  <ul class="notes">
    <li>* Calculated importance found through statistical analysis. Partial Least Squares is used to descover the connection between each business driver and loyalty.</li>
    <li>** Asked importance is found by simply asking customers how important they find each bussiness driver.</li>
  </ul>
</div>
</body>
</html>
```